Ridgeway Provisioning Group needs a cool web design

We need a web design for a new start up called Ridgeway Provisioning Group. RPG is all about working with mine sites to reduce costs and make their supply chains more effective and cost efficient. I have attached our logo and a very basic tile format layout for the website but I will take your advice on best layout. I do prefer a tile based page similar to "Varnholt.com/advisory" this displays a professional yet cool look. The secondary pages need to have the same format.
Target Market(s)
Target customers are typically men in the mining industry. They want simplicity and are time poor.
Industry/Entity Type
Mining
Coding
Coded - Design and coding required
Requirements
Must have
- Must be simple, prefer tile based such as the Varnholts.com/advisory website.
Use bold writing and fonts. No flowery fonts.
Must use corporate colors but don't make too dark.
the site must have connections to well designed second pages.

```html
<!DOCTYPE html>
<html lang="en">
<head>
<meta charset="utf-8">
<title>Ridgeway Provisioning Group</title>
<link href="https://fonts.googleapis.com/css2?family=Bebas+Neue&family=Cabin:wght@500;600&family=Cabin+Condensed:wght@500&family=Arimo:wght@400;700&display=swap" rel="stylesheet">
<style>
  :root{
    --page:#5a5a5a;
    --red:#a51417;
    --red-soft:#c0393b;
    --amber:#f5a800;
    --white:#ffffff;
    --ink:#1c1c1c;
    --panel:rgba(60,58,56,.82);
    --rule:#e0a0a0;
  }
  *{margin:0;padding:0;box-sizing:border-box}
  html,body{width:1200px;height:1000px;overflow:hidden;background:var(--page)}
  body{position:relative;font-family:"Arimo",Arial,sans-serif}
  .abs{position:absolute}

  .brand{left:470px;top:40px;display:flex;align-items:center;gap:14px}
  .brand-mark{width:22px;height:22px;background:var(--red)}
  .brand-name{font-family:"Cabin",sans-serif;font-weight:600;color:var(--white);font-size:19px;line-height:22px;letter-spacing:1px;text-transform:uppercase}

  .utility{left:86px;top:125px}
  .search{left:962px;top:123px;width:124px;height:22px;border:1px solid #7c7c7c;background:#555}
  .search-btn{left:1093px;top:127px}

  .hero{left:86px;top:153px;width:1026px;height:407px;background:linear-gradient(160deg,#6d6d6b 0%,#8b8a86 35%,#a6a5a0 60%,#5f5e5b 100%)}
  .hero-menu{left:86px;top:153px;width:282px;height:407px;background:var(--panel);list-style:none;padding-top:88px}
  .hero-menu li{font-family:"Cabin",sans-serif;font-weight:600;font-size:15px;color:var(--white);height:40px;line-height:20px;display:flex;align-items:center;gap:9px;padding-left:9px}
  .hero-menu li::before{content:"";width:11px;height:6px;background:var(--amber);transform:skewX(-30deg)}
  .dots{left:1025px;top:534px;display:flex;gap:7px}
  .dots span{width:13px;height:13px;border-radius:50%;background:#111}
  .dots span:first-child{background:var(--amber)}

  .content{left:86px;top:560px;width:1026px;height:352px;background:var(--white)}
  .tab{left:1058px;top:565px;width:54px;height:7px;background:#e9ebee}
  .welcome{left:95px;top:584px;font-family:"Bebas Neue",sans-serif;font-size:29px;color:#111;line-height:30px}
  .welcome em{font-style:normal;color:var(--red)}

  .profile-strip{left:86px;top:624px;width:512px;height:8px;background:#eceef0}
  .profile-photo{left:86px;top:632px;width:513px;height:225px;background:radial-gradient(circle at 72% 45%,#f0c070 0%,#b0582a 25%,#5a2c18 55%,#2a1a14 100%)}
  .profile-box{left:86px;top:632px;width:259px;height:154px;background:var(--red);padding:18px 10px 0 10px}
  .profile-box::after{content:"";position:absolute;right:-12px;top:68px;border-left:12px solid var(--red);border-top:12px solid transparent;border-bottom:12px solid transparent}
  .profile-title{font-family:"Bebas Neue",sans-serif;font-size:18px;color:var(--amber);line-height:20px;margin-bottom:9px}
  .profile-text{font-size:12.5px;line-height:18px;color:var(--white);letter-spacing:.4px}
  .more{color:var(--amber);font-size:10px;letter-spacing:.6px}

  .intro{left:607px;top:629px;width:498px;font-size:12.4px;line-height:18px;color:var(--ink);text-align:justify;letter-spacing:.5px}
  .intro .more{color:var(--red);font-size:11.5px}

  .btn{font-family:"Cabin Condensed",sans-serif;font-weight:500;font-size:17px;line-height:25px;padding:0 8px}
  .btn-global{left:671px;top:788px;background:var(--red-soft);color:var(--white)}
  .cases{left:859px;top:744px;width:254px;height:114px;background:radial-gradient(circle at 50% 62%,#e8a040 0%,#7a5a48 22%,#1f5ea8 50%,#0d2a5a 100%)}
  .btn-cases{left:928px;top:789px;background:#d8d4d0;color:var(--red)}

  .foot-rule{left:86px;top:886px;width:1026px;height:1px;background:var(--rule)}
  .foot-links{left:86px;top:891px;width:1026px;text-align:center;font-size:12.5px;color:var(--ink);letter-spacing:.6px;word-spacing:2px}
  .copyright{left:87px;top:929px;font-size:9px;font-weight:700;color:#cfcfcf;letter-spacing:.3px}
  .social{left:1005px;top:924px;display:flex;gap:9px}
  .social span{width:20px;height:20px;background:#8a8a8a}
</style>
</head>
<body>
  <header class="brand abs">
    <span class="brand-mark"></span>
    <span class="brand-name">Ridgeway<br>Provisioning<br>Group</span>
  </header>

  <svg class="utility abs" width="60" height="18" viewBox="0 0 60 18" aria-label="Home and email">
    <path d="M2 9 L8 3.5 L14 9 H12 V14 H4 V9 Z" fill="#f5a800"/>
    <rect x="7" y="10" width="2.5" height="4" fill="#5a5a5a"/>
    <rect x="34.5" y="3.5" width="20" height="12" fill="none" stroke="#f5a800" stroke-width="1.4"/>
    <path d="M34.5 3.5 L44.5 11 L54.5 3.5" fill="none" stroke="#f5a800" stroke-width="1.4"/>
  </svg>
  <div class="search abs"></div>
  <svg class="search-btn abs" width="14" height="14" viewBox="0 0 14 14" aria-label="Search">
    <circle cx="5.5" cy="5.5" r="4" fill="none" stroke="#111" stroke-width="1.8"/>
    <path d="M8.5 8.5 L12 12" stroke="#111" stroke-width="2"/>
  </svg>

  <div class="hero abs" role="img" aria-label="Yellow haul trucks driving through an open-cut mine"></div>
  <ul class="hero-menu abs">
    <li>Procurement Services</li>
    <li>Strategic Sourcing Services</li>
    <li>Lead Time Reduction Services</li>
    <li>Inventory Optimisation Services</li>
    <li>Critical Spare Parts Audit</li>
    <li>Suppy Chain Health Check</li>
  </ul>
  <div class="dots abs"><span></span><span></span><span></span><span></span></div>

  <main class="content abs"></main>
  <div class="tab abs"></div>
  <h1 class="welcome abs">Welcome to <em>Ridgeway Provisioning Group</em></h1>

  <div class="profile-strip abs"></div>
  <div class="profile-photo abs" role="img" aria-label="Lit underground mine tunnel with rail tracks"></div>
  <section class="profile-box abs">
    <h2 class="profile-title">Our Profile</h2>
    <p class="profile-text">Nisl turpis est, vel elit, congue wisi enim nunc ultricies sit, magna tincidunt. Maecenas aliquam maecenas ligula nostra, accumsan taciti. <span class="more">readmore...</span></p>
  </section>

  <p class="intro abs">Praesent integer leo orci aliquam, nibh a. Diam nobis eget, erat natoque integer fringilla viverra. orem ipsum dolor sit amet, ligula nulla pretium, rhoncus tempor placerat fermentum, enim integer ad vestibulum volutpat. isl turpis est, vel elit, congue wisi enim nunc ultricies sit, magna tincidunt.Maecenas aliquam maecenas ligula nostra, accumsan taciti.<br><span class="more">readmore...</span></p>

  <span class="btn btn-global abs">Global Presence</span>
  <div class="cases abs" role="img" aria-label="Blue-lit arched mine tunnel"></div>
  <span class="btn btn-cases abs">Case Studies</span>

  <div class="foot-rule abs"></div>
  <nav class="foot-links abs">Home |&nbsp; About Us |&nbsp; Contact Us &nbsp;| Terms &amp; Conditions &nbsp;|&nbsp; Site Map</nav>
  <p class="copyright abs">Copyright 2015 Ridgeway Provisioning Group. All Rights Reserved.</p>
  <div class="social abs" aria-label="Social links"><span></span><span></span><span></span><span></span></div>
</body>
</html>
```